Copperfox Billboard

Please design a billboard using my photos and logos.
For photo of truck please crop the truck itself out and not have the trees / dirt in photo.
Please put " Best Prices in Sevier County"
Please put " 30-yard Dumpsters Starting at 600.00"
Please put " 16-yard Dumpsters Starting at 300.0"
Please put " Delivery and Pickup 7 Days a week"
Billboard size will be 10 ft tall 30 ft wide

```html
<!DOCTYPE html>
<html lang="en">
<head>
<meta charset="utf-8">
<title>Copperfox Dumpsters Billboard</title>
<link rel="stylesheet" href="https://fonts.googleapis.com/css2?family=Oswald:wght@600&family=Roboto+Condensed:wght@700&display=swap">
<style>
  :root {
    --page-bg: #eceff3;
    --board-light: #f7f7f8;
    --board-mid: #d9d9dc;
    --band-black: #000000;
    --band-purple: #4a1a78;
    --band-purple-dark: #32094f;
    --ink-purple: #2a0b4d;
    --brand-white: #ffffff;
    --card-bg: #ffffff;
    --edge-purple: #4b1a7a;
    --edge-red: #c8202c;
    --edge-blue: #1ea0dc;
    --edge-orange: #f2a325;
  }
  * { box-sizing: border-box; margin: 0; padding: 0; }
  html, body {
    width: 1200px;
    height: 1000px;
    overflow: hidden;
    background: var(--page-bg);
  }
  .billboard {
    position: absolute;
    left: 30px;
    top: 310px;
    width: 1140px;
    height: 380px;
    overflow: hidden;
    background: linear-gradient(160deg, var(--board-mid) 0%, var(--board-light) 45%, var(--board-mid) 100%);
    box-shadow: 0 2px 8px rgba(0,0,0,.18);
  }
  .billboard__waves {
    position: absolute;
    inset: 0;
    width: 100%;
    height: 100%;
  }
  .brand-name {
    position: absolute;
    left: 122px;
    top: 56px;
    width: 336px;
    font-family: "Oswald", sans-serif;
    font-weight: 600;
    color: var(--brand-white);
    text-transform: uppercase;
    line-height: 1;
  }
  .brand-name__main {
    display: block;
    font-size: 62px;
    letter-spacing: 1px;
  }
  .brand-name__sub {
    display: block;
    font-size: 30px;
    letter-spacing: 3px;
    margin-top: 6px;
    padding-left: 120px;
  }
  .offers {
    position: absolute;
    left: 48px;
    top: 192px;
    display: flex;
    gap: 10px;
  }
  .offer-card {
    width: 113px;
    height: 130px;
    background: var(--card-bg);
    border: 2.5px solid;
    border-radius: 12px;
    box-shadow: 2px 3px 4px rgba(0,0,0,.2);
    display: flex;
    align-items: center;
    justify-content: center;
    text-align: center;
    font-family: "Roboto Condensed", sans-serif;
    font-weight: 700;
    font-size: 17px;
    line-height: 1.3;
    color: var(--ink-purple);
    padding: 6px;
  }
  .offer-card--purple { border-color: var(--edge-purple); }
  .offer-card--red { border-color: var(--edge-red); }
  .offer-card--blue { border-color: var(--edge-blue); }
  .offer-card--orange { border-color: var(--edge-orange); }
  .truck-photo {
    position: absolute;
    left: 570px;
    top: 45px;
    width: 513px;
    height: 302px;
    border-radius: 6px;
    background: linear-gradient(90deg, #f2f2f2 0%, #e6e6e8 35%, #5a2d8c 62%, #3a1460 100%);
  }
</style>
</head>
<body>
  <section class="billboard">
    <svg class="billboard__waves" viewBox="0 0 1140 380" preserveAspectRatio="none" aria-hidden="true">
      <path d="M0,0 H790 C620,60 420,100 270,75 C150,55 60,30 0,10 Z" fill="var(--band-black)"/>
      <path d="M0,10 C60,30 150,55 270,75 C420,100 620,60 790,0 H920 C720,90 480,140 290,125 C160,115 60,80 0,65 Z" fill="var(--band-purple)"/>
      <path d="M600,40 C680,25 740,12 790,0 H920 C820,45 720,80 600,105 Z" fill="var(--band-purple-dark)" opacity=".7"/>
    </svg>

    <h1 class="brand-name">
      <span class="brand-name__main">Copperfox</span>
      <span class="brand-name__sub">Dumpsters</span>
    </h1>

    <div class="offers">
      <div class="offer-card offer-card--purple">Best Prices In Sevier County</div>
      <div class="offer-card offer-card--red">30-yard Dumpsters Starting at 600.00</div>
      <div class="offer-card offer-card--blue">16-yard Dumpsters Starting at 300.0</div>
      <div class="offer-card offer-card--orange">Delivery and Pickup 7 Days a week</div>
    </div>

    <div class="truck-photo" role="img" aria-label="Photo of a white roll-off truck carrying a purple dumpster container"></div>
  </section>
</body>
</html>
```